Website design project for ICT Business - Bright Harbour Tx

We need website built for our new startup. The company name is Bright Harbour TX. Bright Harbour is an Information Communication Technology business that aims to help small to medium businesses unlock the power and benefits of the cloud. We are a sales and support business that consults with our clients to assist them in migrating to the cloud safely and without business interruption.

Coding

Coded - Design and coding required

Number of Pages Required

4 page

```html
<!DOCTYPE html>
<html lang="en">
<head>
<meta charset="utf-8">
<title>Bright Harbour TX</title>
<link href="https://fonts.googleapis.com/css2?family=Montserrat:wght@400;500&family=Arimo:wght@400;700&family=Bebas+Neue&family=Lato:ital@1&display=swap" rel="stylesheet">
<style>
:root{
  --navy:#0b5a9f;
  --navy-deep:#0a4f8e;
  --ink:#0d4a82;
  --sky:#14ace8;
  --sky-soft:#2bb6ec;
  --text:#333;
  --muted:#555;
  --white:#fff;
  --grey:#e7e7e7;
}
*{margin:0;padding:0;box-sizing:border-box}
html,body{width:1200px;height:2731px;overflow:hidden;background:var(--white)}
body{position:relative;font-family:Arimo,Arial,sans-serif;color:var(--text)}
.abs{position:absolute}
.display{font-family:Montserrat,Arial,sans-serif;font-weight:400}
.accent{color:var(--sky)}

/* header */
.site-header{left:0;top:0;width:1200px;height:115px;border-top:4px solid var(--navy)}
.brand{left:76px;top:34px;font-family:Montserrat,sans-serif;font-weight:500;font-size:30px;color:var(--navy);display:flex;align-items:center;gap:12px}
.brand-dot{width:26px;height:26px;border-radius:50%;background:var(--navy)}
.nav-home{left:497px;top:0;width:106px;height:115px;background:var(--navy);color:var(--white);font-size:17px;display:flex;align-items:center;justify-content:center}
.nav-link{top:51px;font-size:17px;color:#111}
.search{left:1101px;top:50px}

/* hero */
.hero{left:0;top:115px;width:1200px;height:562px;background:radial-gradient(ellipse at 30% 40%,#3f88d8 0%,#14468a 35%,#0a1a36 70%,#050a14 100%)}
.hero-title{right:76px;top:262px;font-family:"Bebas Neue",sans-serif;font-size:90px;letter-spacing:2px;color:var(--white);line-height:1}
.hero-text{right:76px;top:360px;width:560px;text-align:right;font-family:Lato,sans-serif;font-style:italic;font-size:16px;line-height:27px;color:#d8e4f2}
.hero-btn{left:912px;top:455px;width:208px;height:57px;background:var(--navy);color:var(--white);font-size:20px;display:flex;align-items:center;justify-content:center;border-radius:3px}
.hero-arrow{top:376px;width:52px;height:52px;border:2px solid rgba(255,255,255,.6);border-radius:50%}

/* welcome */
.section-title{font-size:46px;color:var(--ink)}
.welcome-title{left:76px;top:728px}
.welcome-copy{left:76px;top:790px;width:690px;font-size:14.5px;line-height:27px;color:var(--text)}
.welcome-copy p+p{margin-top:4px}
.btn{background:var(--navy);color:var(--white);font-size:20px;display:flex;align-items:center;justify-content:center;border-radius:3px}
.know-more{left:76px;top:969px;width:179px;height:56px}
.welcome-badge{left:800px;top:790px;width:310px;height:170px;display:flex;align-items:center;gap:18px;font-family:Montserrat,sans-serif;font-weight:500;font-size:36px;color:var(--navy)}
.welcome-badge span.dot{width:60px;height:60px;border-radius:50%;background:var(--sky);flex:none}

/* services */
.services-band{left:0;top:1165px;width:1200px;height:383px;background:linear-gradient(#fff,#e2e2e2)}
.services-title{left:0;width:1200px;top:1072px;text-align:center}
.service-card{top:1147px;width:336px;height:401px}
.service-card svg.shape{position:absolute;left:0;top:0}
.service-icon{position:absolute;left:101px;top:72px;width:134px;height:134px;border-radius:50%;background:var(--white);border:4px solid rgba(255,255,255,.5);background-clip:padding-box;display:flex;align-items:center;justify-content:center}
.service-name{position:absolute;left:0;width:336px;top:222px;text-align:center;font-family:Montserrat,sans-serif;font-size:20px;color:var(--sky-soft)}
.card-light .service-name{color:var(--navy-deep)}
.service-text{position:absolute;left:18px;width:300px;top:260px;text-align:center;font-size:14px;line-height:27px;color:var(--white)}
.read-more{position:absolute;left:0;width:336px;top:354px;text-align:center;font-family:Montserrat,sans-serif;font-style:italic;font-size:15px;color:var(--white);text-decoration:underline}

/* news */
.news-title{left:76px;top:1600px}
.view-all{left:1029px;top:1626px;font-size:16px;color:var(--ink);display:flex;align-items:center;gap:10px}
.news-item{top:1668px;width:251px}
.news-photo{width:251px;height:168px}
.news-head{margin-top:22px;font-family:Montserrat,sans-serif;font-size:18px;color:#111}
.news-date{margin-top:10px;font-size:14px;color:var(--sky);display:flex;align-items:center;gap:10px}
.news-text{margin-top:8px;font-size:13.5px;line-height:27px;color:var(--muted)}
.news-text b{color:var(--navy)}

/* testimonials */
.testimonials{left:0;top:2058px;width:1200px;height:322px;background:var(--sky)}
.notch{left:576px;top:2058px}
.testi-title{left:0;width:1200px;top:2128px;text-align:center;color:var(--ink)}
.avatar{left:94px;top:2190px;width:114px;height:114px;border-radius:50%;border:3px solid var(--white);background:linear-gradient(160deg,#e8d7c8,#8c6a55)}
.client{left:244px;top:2221px;color:var(--white);text-align:center}
.client-name{font-family:Montserrat,sans-serif;font-size:20px}
.client-site{font-size:13px;margin-top:6px}
.quote{left:415px;top:2200px;width:700px;padding-left:34px;border-left:3px solid rgba(11,90,159,.5);font-size:14.5px;line-height:27px;color:var(--white)}
.quote-mark{font-family:Georgia,serif;font-size:34px;color:var(--white)}
.dots{left:556px;top:2317px;display:flex;gap:12px}
.dots span{width:14px;height:14px;border-radius:50%;background:var(--navy)}
.dots span.on{background:#d9d9d9;border:2px solid var(--navy)}

/* footer */
.site-footer{left:0;top:2380px;width:1200px;height:351px;background:var(--navy)}
.footer-rule{left:0;top:2672px;width:1200px;height:1px;background:rgba(255,255,255,.12)}
.footer-brand{left:91px;top:2450px;width:190px;font-family:Montserrat,sans-serif;font-weight:500;font-size:30px;line-height:38px;color:var(--white);display:flex;gap:14px;align-items:center}
.footer-brand .dot{width:26px;height:26px;border-radius:50%;background:var(--white);flex:none}
.social{top:2549px;width:40px;height:40px;border-radius:50%}
.social.solid{background:var(--sky)}
.social.ring{border:2px solid rgba(255,255,255,.55)}
.footer-head{top:2412px;font-family:Montserrat,sans-serif;font-size:17px;color:var(--sky-soft)}
.sitemap{left:319px;top:2448px;list-style:none;font-size:14px;line-height:29px;color:var(--white)}
.sitemap li:first-child{color:var(--sky-soft)}
.contact{left:579px;top:2448px;width:230px;font-size:14px;line-height:24px;color:var(--white)}
.contact-row{display:flex;gap:14px;align-items:flex-start;margin-bottom:10px}
.contact-row svg{flex:none;margin-top:3px}
.contact-row .name{color:var(--sky-soft)}
.field{left:874px;width:237px;background:#eee;font-size:12px;color:#555;padding:6px 7px}
.send{left:874px;top:2600px;width:237px;height:41px;border:2px solid var(--white);color:var(--white);font-size:19px;display:flex;align-items:center;justify-content:center;border-radius:2px}
.copyright{left:0;width:1200px;top:2694px;text-align:center;font-size:14px;color:var(--white)}
.copyright span{color:var(--sky-soft)}
</style>
</head>
<body>

<header class="site-header abs">
  <div class="brand abs"><span class="brand-dot"></span>Bright Harbour</div>
  <div class="nav-home abs">HOME</div>
  <div class="nav-link abs" style="left:637px">ABOUT US</div>
  <div class="nav-link abs" style="left:757px">SERVICES</div>
  <div class="nav-link abs" style="left:876px">NEWS</div>
  <div class="nav-link abs" style="left:960px">CONTACT US</div>
  <svg class="search abs" width="22" height="22" viewBox="0 0 22 22"><circle cx="9" cy="9" r="6.5" fill="none" stroke="#14ace8" stroke-width="3"/><line x1="14" y1="14" x2="20" y2="20" stroke="#14ace8" stroke-width="3.5" stroke-linecap="round"/></svg>
</header>

<section class="hero abs" role="img" aria-label="Photo of a hand holding a glowing world map with network connections"></section>
<div class="hero-arrow abs" style="left:10px"><svg width="48" height="48" viewBox="0 0 48 48"><polyline points="27,15 19,24 27,33" fill="none" stroke="#fff" stroke-width="2"/></svg></div>
<div class="hero-arrow abs" style="left:1136px"><svg width="48" height="48" viewBox="0 0 48 48"><polyline points="21,15 29,24 21,33" fill="none" stroke="#fff" stroke-width="2"/></svg></div>
<h1 class="hero-title abs">BRIGHT HARBOUR</h1>
<p class="hero-text abs">Lorem Ipsum is simply dummy text of the printing and typesetting industry. Lorem Ipsum has been the industry's standard dummy text ever since the 1500s, when an unknown printer took a galley of type.</p>
<div class="hero-btn abs">CONTACT US</div>

<h2 class="section-title display welcome-title abs">Welcome to <span class="accent">Keelson Enterprises</span></h2>
<div class="welcome-copy abs">
  <p>Lorem Ipsum is simply dummy text of the printing and typesetting industry. Lorem Ipsum has been the industry's standard dummy text ever since the 1500s, when an unknown printer took a galley of type and scrambled it to make a type specimen book. It has survived not only five centuries, but also the leap into electronic typesetting, remaining essentially unchanged.</p>
  <p>It was popularised in the 1960s with the release of Dryline sheets containing Lorem Ipsum passages, and more recently with desktop publishing software like Folio Layout including.</p>
</div>
<div class="btn know-more abs">KNOW MORE</div>
<div class="welcome-badge abs"><span class="dot"></span>Bright Harbour</div>

<h2 class="section-title display services-title abs">Our Best <span class="accent">Services</span></h2>
<div class="services-band abs"></div>

<article class="service-card abs" style="left:76px">
  <svg class="shape" width="336" height="401" viewBox="0 0 336 401"><path d="M0 38 Q170 -5 336 0 V401 H0 Z" fill="#0b5a9f"/></svg>
  <div class="service-icon"><svg width="70" height="70" viewBox="0 0 70 70" fill="none" stroke="#0b5a9f" stroke-width="3"><rect x="14" y="10" width="42" height="30" rx="2"/><rect x="8" y="36" width="18" height="26" rx="2"/><rect x="44" y="34" width="18" height="28" rx="2"/><line x1="26" y1="50" x2="44" y2="50"/></svg></div>
  <div class="service-name">ICT PROJECTS</div>
  <p class="service-text">Lorem Ipsum is simply dummy text of the printing and typesetting industry Lorem Ipsum has been the industry's standard</p>
  <div class="read-more">READ MORE</div>
</article>

<article class="service-card card-light abs" style="left:433px">
  <svg class="shape" width="336" height="401" viewBox="0 0 336 401"><path d="M0 18 Q168 -10 336 18 V401 H0 Z" fill="#14ace8"/></svg>
  <div class="service-icon"><svg width="70" height="70" viewBox="0 0 70 70" fill="none" stroke="#14ace8" stroke-width="3"><circle cx="22" cy="22" r="9"/><circle cx="48" cy="30" r="11"/><circle cx="28" cy="52" r="9"/><line x1="29" y1="27" x2="38" y2="28"/><line x1="26" y1="31" x2="27" y2="43"/></svg></div>
  <div class="service-name">ICT ARCHITECTURE</div>
  <p class="service-text">Lorem Ipsum is simply dummy text of the printing and typesetting industry Lorem Ipsum has been the industry's standard</p>
  <div class="read-more">READ MORE</div>
</article>

<article class="service-card abs" style="left:789px">
  <svg class="shape" width="336" height="401" viewBox="0 0 336 401"><path d="M0 0 Q166 -5 336 38 V401 H0 Z" fill="#0b5a9f"/></svg>
  <div class="service-icon"><svg width="70" height="70" viewBox="0 0 70 70" fill="#0b5a9f" stroke="#0b5a9f" stroke-width="3"><circle cx="35" cy="20" r="8"/><path d="M22 42 Q35 26 48 42 Z"/><line x1="35" y1="42" x2="35" y2="56"/><line x1="10" y1="40" x2="22" y2="40"/><line x1="48" y1="40" x2="60" y2="40"/><circle cx="10" cy="40" r="4"/><circle cx="60" cy="40" r="4"/><circle cx="35" cy="58" r="4"/></svg></div>
  <div class="service-name">CLOUD CONSULTATION</div>
  <p class="service-text">Lorem Ipsum is simply dummy text of the printing and typesetting industry Lorem Ipsum has been the industry's standard</p>
  <div class="read-more">READ MORE</div>
</article>

<h2 class="section-title display news-title abs">Latest <span class="accent">News</span></h2>
<div class="view-all abs">View All <svg width="22" height="12" viewBox="0 0 22 12"><path d="M0 6 H20 M15 1 L20 6 L15 11" fill="none" stroke="#0d4a82" stroke-width="1.6"/></svg></div>

<article class="news-item abs" style="left:76px">
  <div class="news-photo" role="img" aria-label="Photo of business people shaking hands by a bright window" style="background:linear-gradient(135deg,#c9dff2,#5d86b0 60%,#1e3d62)"></div>
  <h3 class="news-head">Lorem ipsum is simple text.</h3>
  <div class="news-date"><svg width="13" height="13" viewBox="0 0 13 13"><rect x="1" y="2" width="11" height="10" fill="none" stroke="#14ace8" stroke-width="1.6"/><rect x="1" y="2" width="11" height="3" fill="#14ace8"/></svg>23 dec 2016</div>
  <p class="news-text">Lorem Ipsum is simply dummy text of the printing and the typesetting industry. Lorem Ipsum is..<b>»</b></p>
</article>
<article class="news-item abs" style="left:342px">
  <div class="news-photo" role="img" aria-label="Photo of a hand typing on a laptop with cloud icons" style="background:linear-gradient(135deg,#1a4f9c,#3e8fe0 55%,#c7d9ee)"></div>
  <h3 class="news-head">Lorem ipsum is simple text.</h3>
  <div class="news-date"><svg width="13" height="13" viewBox="0 0 13 13"><rect x="1" y="2" width="11" height="10" fill="none" stroke="#14ace8" stroke-width="1.6"/><rect x="1" y="2" width="11" height="3" fill="#14ace8"/></svg>24 dec 2016</div>
  <p class="news-text">Lorem Ipsum is simply dummy text of the printing and the typesetting industry. Lorem Ipsum is..<b>»</b></p>
</article>
<article class="news-item abs" style="left:610px">
  <div class="news-photo" role="img" aria-label="Photo of a businessman touching a glowing network screen" style="background:linear-gradient(135deg,#0d2c52,#3a7dbf 55%,#a9cbe8)"></div>
  <h3 class="news-head">Lorem ipsum is simple text.</h3>
  <div class="news-date"><svg width="13" height="13" viewBox="0 0 13 13"><rect x="1" y="2" width="11" height="10" fill="none" stroke="#14ace8" stroke-width="1.6"/><rect x="1" y="2" width="11" height="3" fill="#14ace8"/></svg>25 dec 2016</div>
  <p class="news-text">Lorem Ipsum is simply dummy text of the printing and the typesetting industry. Lorem Ipsum is..<b>»</b></p>
</article>
<article class="news-item abs" style="left:874px">
  <div class="news-photo" role="img" aria-label="Photo of a team gathered around a laptop in an office" style="background:linear-gradient(135deg,#5a6f85,#b9c8d6 50%,#e9eef2)"></div>
  <h3 class="news-head">Lorem ipsum is simple text.</h3>
  <div class="news-date"><svg width="13" height="13" viewBox="0 0 13 13"><rect x="1" y="2" width="11" height="10" fill="none" stroke="#14ace8" stroke-width="1.6"/><rect x="1" y="2" width="11" height="3" fill="#14ace8"/></svg>26 dec 2016</div>
  <p class="news-text">Lorem Ipsum is simply dummy text of the printing and the typesetting industry. Lorem Ipsum is..<b>»</b></p>
</article>

<section class="testimonials abs"></section>
<svg class="notch abs" width="48" height="24" viewBox="0 0 48 24"><polygon points="0,0 48,0 24,24" fill="#fff"/></svg>
<h2 class="section-title display testi-title abs">Testimonials</h2>
<div class="avatar abs" role="img" aria-label="Client portrait photo"></div>
<div class="client abs"><div class="client-name">Client Name</div><div class="client-site">something.com</div></div>
<blockquote class="quote abs"><span class="quote-mark">“</span> Lorem Ipsum is simply dummy text of the printing and typesetting industry. Lorem Ipsum has been the industry's standard dummy text ever since the 1500s, when an unknown printer took a galley of type and scrambled it to make a type specimen book. <span class="quote-mark">”</span></blockquote>
<div class="dots abs"><span class="on"></span><span></span><span></span><span></span></div>

<footer class="site-footer abs"></footer>
<div class="footer-brand abs"><span class="dot"></span>Bright Harbour</div>
<div class="social solid abs" style="left:77px"></div>
<div class="social ring abs" style="left:128px"></div>
<div class="social ring abs" style="left:179px"></div>
<div class="social ring abs" style="left:230px"></div>

<div class="footer-head abs" style="left:319px">SITEMAP</div>
<ul class="sitemap abs"><li>» Home</li><li>» About Us</li><li>» Service</li><li>» News</li><li>» Contact Us</li></ul>

<div class="footer-head abs" style="left:579px">GET IN TOUCH</div>
<div class="contact abs">
  <div class="contact-row"><svg width="20" height="24" viewBox="0 0 20 24"><path d="M10 22 C4 14 2 11 2 8 A8 8 0 0 1 18 8 C18 11 16 14 10 22 Z" fill="none" stroke="#2bb6ec" stroke-width="1.6"/><circle cx="10" cy="8" r="3" fill="none" stroke="#2bb6ec" stroke-width="1.6"/></svg><div><span class="name">Bright Harbour</span><br>101- Lorem ipsum is simple dummy text of printing and typeing industry.</div></div>
  <div class="contact-row"><svg width="20" height="20" viewBox="0 0 20 20"><path d="M4 2 L8 2 L9 7 L6.5 8.5 A11 11 0 0 0 11.5 13.5 L13 11 L18 12 L18 16 A2 2 0 0 1 16 18 A15 15 0 0 1 2 4 A2 2 0 0 1 4 2 Z" fill="none" stroke="#2bb6ec" stroke-width="1.5"/></svg>+123 555 0190</div>
  <div class="contact-row"><svg width="20" height="16" viewBox="0 0 20 16"><rect x="1" y="2" width="18" height="12" fill="none" stroke="#2bb6ec" stroke-width="1.6"/><polyline points="1,2 10,9 19,2" fill="none" stroke="#2bb6ec" stroke-width="1.6"/></svg>info@brightharbour.com</div>
  <div class="contact-row"><svg width="20" height="20" viewBox="0 0 20 20"><circle cx="10" cy="10" r="9" fill="#2bb6ec"/><path d="M1 10 H19 M10 1 C5 6 5 14 10 19 M10 1 C15 6 15 14 10 19" fill="none" stroke="#0b5a9f" stroke-width="1.3"/></svg>www.brightharbour.com</div>
</div>

<div class="footer-head abs" style="left:874px">GET A FREE QUOTE</div>
<div class="field abs" style="top:2449px;height:37px">Name</div>
<div class="field abs" style="top:2493px;height:35px">E-Mail</div>
<div class="field abs" style="top:2531px;height:62px">Message</div>
<div class="send abs">SEND</div>

<div class="footer-rule abs"></div>
<p class="copyright abs">©<span>Bright Harbour Texas</span> - 2016. All Rights Reserved</p>

</body>
</html>
```